Brisk Hollow Builders Needs A Flyer

We need a flyer for our newest product "The Cedarlane Garden Workroom"

Here is some copy for the flyer:

1. More and more people everyday are working from home and finding it difficult to disconnect from home activities in order to focus on their work. They are also finding it very expensive to add on to their existing house for a quiet place. Our archatectually stunning, Cedarlane Garden Workroom is the answer. The office studio measures 16' wide and 10' deep. 160 Square feet of space.

Perfect for dozens of purposes. Home office, design studio, artist studio, home school office, reading room, craft studio, drafting room.

Features include:

- Steel Framing. 40-60% lighter then wood, higher strength to weight ratio, resistant to mold and fire and steel is the most recycled material on earth!
- Spray foam insulation. Cool in the summer and warm in the winter.
- HVAC Mini Split with wireless remote control and thermostat.
- 100% Off grid with enough solar and battery storage to run your entire office. No need to pay for an expensive electric installation.
- Flush fitting floor outlets to reduce wires.
- TV mount (Optional with pre-wired electric, HDMI, digital audio & Cat 6)
- Windows are tempered glass custom made by Morvik Glazing.
- Solar qualifies for a 26% tax credit. This is not a write-off rather it is a direct reduction on your tax obligation.
- Thousands of dollars less than adding onto your home.
- Custom color, siding, features available.

This beautiful back yard office is delivered 100% assembled and ready to enjoy on the day of delivery.

We ship nationwide from our factory in South Carolina. Give us a call anytime to speak to a designer and start your dream office today!

555-318-4027
info@BriskHollowBuilders.example

```html
<!DOCTYPE html>
<html lang="en">
<head>
<meta charset="utf-8">
<title>Brisk Hollow Builders – Cedarlane Garden Workroom Flyer</title>
<link rel="stylesheet" href="https://fonts.googleapis.com/css2?family=Lato:wght@400;700;900&family=Ubuntu:wght@500;700&family=Roboto+Condensed:wght@400&family=Roboto:wght@900&display=swap">
<style>
  :root{
    --backdrop:#fdc68a;
    --paper:#ffffff;
    --lime:#c8e03c;
    --lime-soft:#e6f29a;
    --leaf:#1f7a2c;
    --leaf-dark:#17622a;
    --red:#e0201b;
    --ink:#222222;
    --brown:#4f3a1a;
    --brand:#d98a12;
    --ray:#fbe5d6;
    --highlight:#fff200;
  }
  *{box-sizing:border-box;margin:0;padding:0}
  html,body{width:1200px;height:1200px;overflow:hidden}
  body{background:var(--backdrop);position:relative;font-family:"Lato",sans-serif;color:var(--ink)}

  .page{position:absolute;top:201px;width:544px;height:768px;background:var(--paper);overflow:hidden}
  .page--front{left:38px}
  .page--back{left:618px}
  .page svg.frame{position:absolute;inset:0;width:544px;height:768px}

  /* brand */
  .brand{position:absolute;display:flex;align-items:center;gap:6px;font-family:"Ubuntu",sans-serif;font-weight:700;color:var(--brand);font-size:15px;line-height:1.05;width:130px}
  .brand__dot{flex:none;width:16px;height:16px;border-radius:50%;background:var(--leaf)}
  .page--front .brand{left:30px;top:50px}
  .page--back .brand{left:396px;top:50px}

  /* front title */
  .title{position:absolute;left:192px;top:24px;width:230px;text-align:center;font-family:"Ubuntu",sans-serif;line-height:.95}
  .title__the{color:var(--leaf-dark);font-weight:500;font-size:27px}
  .title__red{color:var(--red);font-weight:700;font-size:33px;display:block}
  .title__green{color:var(--leaf-dark);font-weight:500;font-size:24px;display:block;margin-top:3px}

  .intro{position:absolute;left:48px;top:177px;width:447px;font-size:12.2px;line-height:15.6px;text-align:justify}
  .intro p+p{margin-top:11px}

  .highlights{position:absolute;left:86px;top:616px;width:400px;list-style:none;font-weight:700;font-size:12px;line-height:15.5px;color:var(--brown)}
  .highlights li{position:relative;padding-left:13px}
  .highlights li+li{margin-top:3px}
  .highlights li::before{content:"";position:absolute;left:0;top:5px;width:5px;height:5px;border-radius:50%;background:var(--leaf)}

  .callbar{position:absolute;left:0;top:677px;width:544px;height:15px;background:var(--red);color:#fff;font-weight:700;font-size:11.6px;line-height:15px;padding-left:48px}

  .contact{position:absolute;left:48px;top:704px;width:490px;display:flex;align-items:center;gap:4px;white-space:nowrap}
  .contact__small{font-family:"Roboto Condensed",sans-serif;font-size:8.4px}
  .contact__phone{font-family:"Roboto",sans-serif;font-weight:900;font-size:29px;letter-spacing:-.3px;line-height:1}

  /* back */
  .features-head{position:absolute;left:37px;top:50px;width:258px;height:21px;background:linear-gradient(90deg,var(--highlight) 0%,var(--highlight) 10%,rgba(255,242,0,.35) 70%,rgba(255,255,255,0) 100%)}
  .features-head h2{font-family:"Lato",sans-serif;font-weight:900;font-size:17px;color:var(--leaf);line-height:21px;padding-left:30px}

  .features{position:absolute;left:49px;top:80px;width:450px;list-style:none;font-size:11.4px;line-height:15.5px}
  .features li{position:relative;padding-left:13px;margin-bottom:15.5px}
  .features li:first-child{width:285px;text-align:justify}
  .features li::before{content:"";position:absolute;left:0;top:6px;width:4px;height:4px;border-radius:50%;background:var(--leaf)}
  .features strong{color:var(--red);font-weight:700}

  .gallery{position:absolute;left:46px;top:447px;width:452px;display:grid;grid-template-columns:224px 224px;column-gap:4px;row-gap:0}
  .gallery figure{margin:0}
  .gallery .shot{height:126px;border:1.6px solid var(--leaf)}
  .gallery figcaption{font-family:"Roboto Condensed",sans-serif;font-size:8px;color:var(--leaf);text-align:center;text-transform:uppercase;height:14px;line-height:14px}
  .shot--front-persp{background:linear-gradient(180deg,#bcd6ea 0%,#6f8d55 45%,#3d5a2c 100%)}
  .shot--back-persp{background:linear-gradient(180deg,#c7ddef 0%,#7b9568 45%,#4a6335 100%)}
  .shot--front{background:linear-gradient(180deg,#ffffff 0%,#e9e6e0 40%,#3b3b3b 100%)}
  .shot--frame{background:linear-gradient(180deg,#ffffff 0%,#dcdcdc 55%,#ffffff 100%)}
</style>
</head>
<body>

<section class="page page--front" aria-label="Flyer front">
  <svg class="frame" viewBox="0 0 544 768" aria-hidden="true">
    <defs>
      <radialGradient id="rays" cx="0.6" cy="0.08" r="0.55">
        <stop offset="0" stop-color="var(--ray)"/>
        <stop offset="1" stop-color="#ffffff"/>
      </radialGradient>
      <linearGradient id="greenFade" x1="0" y1="0" x2="1" y2="0">
        <stop offset="0" stop-color="var(--lime)"/>
        <stop offset=".25" stop-color="#ffffff"/>
        <stop offset=".75" stop-color="#ffffff"/>
        <stop offset="1" stop-color="var(--lime)"/>
      </linearGradient>
      <linearGradient id="gardenTones" x1="0" y1="0" x2="0" y2="1">
        <stop offset="0" stop-color="#b9d4ea"/>
        <stop offset=".4" stop-color="#5f7f45"/>
        <stop offset="1" stop-color="#3e5b2b"/>
      </linearGradient>
    </defs>
    <rect width="544" height="320" fill="url(#rays)"/>
    <circle cx="70" cy="38" r="116" fill="#fff" stroke="var(--lime)" stroke-width="6"/>
    <circle cx="310" cy="51" r="120" fill="#fff" stroke="var(--lime)" stroke-width="6"/>
    <rect y="590" width="544" height="90" fill="url(#greenFade)"/>
    <polygon points="0,307 544,330 544,614 0,595" fill="url(#gardenTones)" stroke="var(--leaf-dark)" stroke-width="2" role="img" aria-label="Rendered photo of the dark-clad garden workroom with glass front and furnished office interior in a leafy backyard"/>
    <rect y="692" width="544" height="39" fill="#ffffff"/>
    <rect y="692" width="544" height="39" fill="url(#greenFade)" opacity=".5"/>
    <rect y="731" width="544" height="37" fill="var(--lime)"/>
  </svg>

  <div class="brand"><span class="brand__dot"></span>Brisk Hollow Builders</div>

  <h1 class="title">
    <span class="title__the">The</span>
    <span class="title__red">Cedarlane Garden</span>
    <span class="title__green">Workroom</span>
  </h1>

  <div class="intro">
    <p>More and more people everyday are working from home and finding it difficult to disconnect from home activities in order to focus on their work. They are also finding it very expensive to add on to their existing house for a quiet place. Our archatectually stunning, Cedarlane Garden Workroom is the answer. The office studio measures 16' wide and 10' deep. 160 Square feet of space.</p>
    <p>Perfect for dozens of purposes. Home office, design studio, artist studio, home school office, reading room, craft studio, drafting room.</p>
  </div>

  <ul class="highlights">
    <li>This beautiful back yard office is delivered 100% assembled and ready to enjoy on the day of delivery.</li>
    <li>We ship nationwide from our factory in South Carolina.</li>
  </ul>

  <div class="callbar">Give us a call anytime to speak to a designer and start your dream office today!</div>

  <div class="contact">
    <span class="contact__small">www.BriskHollowBuilders.example</span>
    <span class="contact__phone">555-318-4027</span>
    <span class="contact__small">info@BriskHollowBuilders.example</span>
  </div>
</section>

<section class="page page--back" aria-label="Flyer back">
  <svg class="frame" viewBox="0 0 544 768" aria-hidden="true">
    <defs>
      <linearGradient id="sideFade" x1="0" y1="0" x2="0" y2="1">
        <stop offset="0" stop-color="var(--lime)"/>
        <stop offset=".6" stop-color="var(--lime-soft)"/>
        <stop offset="1" stop-color="#ffffff"/>
      </linearGradient>
    </defs>
    <rect width="544" height="37" fill="var(--lime)"/>
    <rect width="37" height="768" fill="var(--lime)"/>
    <rect x="507" width="37" height="768" fill="url(#sideFade)"/>
    <rect y="731" width="544" height="37" fill="var(--lime)"/>
    <circle cx="460" cy="40" r="108" fill="#fff" stroke="var(--lime)" stroke-width="6"/>
  </svg>

  <div class="brand"><span class="brand__dot"></span>Brisk Hollow Builders</div>

  <div class="features-head"><h2>Features include:</h2></div>

  <ul class="features">
    <li><strong>Steel Framing.</strong> 40-60% lighter then wood, higher strength to weight ratio, resistant to mold and fire and steel is the most recycled material on earth!</li>
    <li><strong>Spray foam insulation.</strong> Cool in the summer and warm in the winter.</li>
    <li><strong>HVAC Mini Split</strong> with wireless remote control and thermostat.</li>
    <li><strong>100% Off grid</strong> with enough solar and battery storage to run your entire office. No need to pay for an expensive electric installation.</li>
    <li><strong>Flush fitting</strong> floor outlets to reduce wires.</li>
    <li><strong>TV mount</strong> (Optional with pre-wired electric, HDMI, digital audio &amp; Cat 6)</li>
    <li>Windows are <strong>tempered glass</strong> custom made by Morvik Glazing.</li>
    <li>Solar qualifies for a <strong>26% tax credit</strong>. This is not a write-off rather it is a direct reduction on your tax obligation.</li>
    <li><strong>Thousands of dollars less</strong> than adding onto your home.</li>
    <li><strong>Custom color, siding, features</strong> available.</li>
  </ul>

  <div class="gallery">
    <figure><div class="shot shot--front-persp" role="img" aria-label="Front perspective render of the workroom in a garden"></div><figcaption>Front view (perspective)</figcaption></figure>
    <figure><div class="shot shot--back-persp" role="img" aria-label="Back perspective render showing the roof solar panels"></div><figcaption>Back view (perspective)</figcaption></figure>
    <figure><div class="shot shot--front" role="img" aria-label="Front view render of the workroom on a white background"></div><figcaption>Front view</figcaption></figure>
    <figure><div class="shot shot--frame" role="img" aria-label="Exploded technical drawing of the steel frame"></div><figcaption>Stee frame exploded view</figcaption></figure>
  </div>
</section>

</body>
</html>
```